Stationary Set Rebrand for Brenvik

We are a Canadian Distribution and Service Company that was established in 1969. Over the past 5 decades we have expanded our business and have warehouses across Canada. We specialize in adhesive tapes, adhesives, films, safety, warehouse, shipping, janitorial and packaging supplies.

We have updated our logo design and would like a new corporate branding identity that includes a new fresh Stationary Set (Business Cards, Letterhead, Letterhead MS Word, Envelope, Presentation Folders, Email Signatures, Notepad Covers, etc.)

Target Market(s)

Industrial Business Sector

Font styles to use
Sans Serif

Colors
0054AA
0677BA
7BADD7
CADEEF
E8F1F8
0094D4
00A9DD
6FCCEA
C7EBF8
E9F6FB
00AB8E
00BBA5
67D7C9
C6EFE9
E9F9F6
EB3D1F
EC4F4E
F09395
F8D3D4
FCEDEE

Requirements
Should not have
• Colors not too light, darker colours preferred

```html
<!DOCTYPE html>
<html lang="en">
<head>
<meta charset="utf-8">
<title>Brenvik Stationery Set</title>
<link rel="stylesheet" href="https://fonts.googleapis.com/css2?family=Arimo:wght@400;700&family=Barlow+Condensed:wght@500&display=swap">
<style>
:root{
  --bg:#e6e6e6;
  --ink:#0d0d0d;
  --paper:#ffffff;
  --red:#d93236;
  --rule:#a9a9a9;
  --text:#333333;
  --sign:#9a9a9a;
}
*{margin:0;padding:0;box-sizing:border-box}
html,body{width:1200px;height:960px;overflow:hidden;background:var(--bg)}
body{position:relative;font-family:Arimo,Arial,sans-serif;color:var(--text)}
.item{position:absolute}
.wordmark{font-family:Arimo,Arial,sans-serif;font-weight:700;color:var(--ink);line-height:1;letter-spacing:-0.01em}
.wordmark.on-dark{color:var(--paper)}
.tagline{font-family:"Barlow Condensed","Arial Narrow",sans-serif;font-weight:500;color:var(--ink);line-height:1}
.tagline.on-dark{color:var(--paper)}
.band{position:absolute;left:0;right:0;bottom:0;display:flex}
.band .black{background:var(--ink);flex:0 0 58%;clip-path:polygon(0 0,100% 0,calc(100% - 6px) 100%,0 100%)}
.band .red{background:var(--red);flex:1;margin-left:-3px;clip-path:polygon(6px 0,100% 0,100% 100%,0 100%)}
.contact{font-size:5px;line-height:1.45;color:var(--ink)}
.contact .row{display:flex;align-items:center;gap:4px}
.contact .dot{width:5px;height:5px;border-radius:50%;background:var(--ink);flex:none}
.contact .gap{height:3px}

/* hero lockup */
.hero{left:404px;top:70px;width:392px;text-align:center}
.hero .wordmark{font-size:92px}
.hero .tagline{font-size:22px;margin-top:4px}

/* letterhead */
.letterhead{left:179px;top:274px;width:289px;height:406px;background:var(--paper)}
.letterhead .brand{position:absolute;left:28px;top:28px}
.letterhead .brand .wordmark{font-size:26px}
.letterhead .brand .tagline{font-size:6.5px;margin-top:1px}
.letterhead .contact{position:absolute;left:209px;top:23px}
.letterhead .letter{position:absolute;left:11px;top:101px;width:270px;font-size:5.6px;line-height:1.2}
.letterhead .letter p{margin-bottom:6px}
.letterhead .signature{width:50px;height:14px;background:var(--sign);opacity:.35;margin:14px 0 5px 3px;border-radius:2px}
.letterhead .signer{margin-left:3px;font-size:6px}
.letterhead .band{height:10px}

/* folder */
.folder{left:488px;top:250px;width:313px;height:432px;background:var(--ink)}
.folder .brand{position:absolute;left:0;right:0;top:186px;text-align:center}
.folder .wordmark{font-size:44px}
.folder .tagline{font-size:10px;margin-top:3px}

/* business cards */
.card{top:333px;width:116px;height:67px}
.card-front{left:843px;background:var(--paper)}
.card-front .brand{position:absolute;left:9px;top:28px}
.card-front .wordmark{font-size:12px}
.card-front .tagline{font-size:3.2px;margin-top:1px}
.card-front .contact{position:absolute;left:62px;top:21px;font-size:3px}
.card-front .contact .dot{width:3px;height:3px}
.card-front .contact .row{gap:3px}
.card-front .contact .gap{height:2px}
.card-front .band{height:5px}
.card-back{left:972px;background:var(--ink)}
.card-back .brand{position:absolute;left:0;right:0;top:22px;text-align:center}
.card-back .wordmark{font-size:17px}
.card-back .tagline{font-size:4.2px;margin-top:1px}

/* notepad */
.notepad{left:896px;top:438px;width:173px;height:240px;background:var(--paper)}
.notepad .coil{position:absolute;left:8px;right:8px;top:-4px;height:12px}
.notepad .lines{position:absolute;left:3px;right:3px;top:55px}
.notepad .lines span{display:block;height:16px;border-bottom:1px solid var(--rule)}
.notepad .band{height:8px}

/* compliment slip */
.slip{left:233px;top:710px;width:300px;height:136px;background:var(--paper)}
.slip .brand{position:absolute;left:18px;top:16px}
.slip .wordmark{font-size:15px}
.slip .tagline{font-size:4px;margin-top:1px}
.slip .contact{position:absolute;left:17px;top:74px}
.slip .band{height:10px}

/* envelope */
.envelope{left:557px;top:709px;width:299px;height:137px;background:var(--paper)}
.envelope .flap{position:absolute;left:0;top:0;width:299px;height:37px}
.envelope .brand{position:absolute;left:0;right:0;top:9px;text-align:center}
.envelope .wordmark{font-size:15px}
.envelope .tagline{font-size:4px;margin-top:1px}
</style>
</head>
<body>

<section class="item hero">
  <div class="wordmark">Brenvik</div>
  <div class="tagline">Tape and Packaging Specialists</div>
</section>

<article class="item letterhead">
  <div class="brand">
    <div class="wordmark">Brenvik</div>
    <div class="tagline">Tape and Packaging Specialists</div>
  </div>
  <div class="contact">
    <div>418 Kestrel Row</div>
    <div>Halden, ON L4K 2R9</div>
    <div class="gap"></div>
    <div class="row"><span class="dot"></span>905 555 0147</div>
    <div class="row"><span class="dot"></span>mara.quell@brenvik.com</div>
    <div class="row"><span class="dot"></span>www.brenvik.com</div>
  </div>
  <div class="letter">
    <p>Your Ref: SP KMC</p>
    <p>1 Dec 2014</p>
    <p style="margin-bottom:22px">Mr Name of client<br>Designantion<br>Norhaven Group ltd.<br>Level 10<br>Address<br>WESTFORD ON 3000</p>
    <p>Thank you for the opportunity of providing a proposal regarding the form and nature of assistance we can provide to you with the development of the Norhaven Group ltd website our company commitment to providing innovative online solutions to the web developments required by organisations is the key to our success. We believe the benefits of our methodology and experience with a broad spectrum of web projects puts us in a strong position to assist you.</p>
    <p>We realise the importance of this project to Harbourline Freight and look forward to the opportunity of contributing and working with you.</p>
    <p>Thank you for the opportunity of providing a proposal regarding the form and nature of assistance we can provide to you with the development of the Norhaven Group ltd website our company commitment to providing innovative online solutions to the web developments required by</p>
    <div class="signature" role="img" aria-label="Handwritten signature of Mara Quell"></div>
    <div class="signer">Mara Quell</div>
  </div>
  <div class="band"><span class="black"></span><span class="red"></span></div>
</article>

<article class="item folder">
  <div class="brand">
    <div class="wordmark on-dark">Brenvik</div>
    <div class="tagline on-dark">Tape and Packaging Specialists</div>
  </div>
</article>

<article class="item card card-front">
  <div class="brand">
    <div class="wordmark">Brenvik</div>
    <div class="tagline">Tape and Packaging Specialists</div>
  </div>
  <div class="contact">
    <div>418 Kestrel Row</div>
    <div>Halden, ON L4K 2R9</div>
    <div class="gap"></div>
    <div class="row"><span class="dot"></span>905 555 0147</div>
    <div class="row"><span class="dot"></span>mara.quell@brenvik.com</div>
    <div class="row"><span class="dot"></span>www.brenvik.com</div>
  </div>
  <div class="band"><span class="black"></span><span class="red"></span></div>
</article>

<article class="item card card-back">
  <div class="brand">
    <div class="wordmark on-dark">Brenvik</div>
    <div class="tagline on-dark">Tape and Packaging Specialists</div>
  </div>
</article>

<article class="item notepad">
  <svg class="coil" viewBox="0 0 157 12" aria-hidden="true">
    <g fill="none" stroke="#0d0d0d" stroke-width="1.3">
      <path d="M4 0v8M16 0v8M28 0v8M40 0v8M52 0v8M64 0v8M76 0v8M88 0v8M100 0v8M112 0v8M124 0v8M136 0v8M148 0v8"/>
    </g>
    <g fill="#0d0d0d">
      <circle cx="4" cy="9" r="2.4"/><circle cx="16" cy="9" r="2.4"/><circle cx="28" cy="9" r="2.4"/><circle cx="40" cy="9" r="2.4"/><circle cx="52" cy="9" r="2.4"/><circle cx="64" cy="9" r="2.4"/><circle cx="76" cy="9" r="2.4"/><circle cx="88" cy="9" r="2.4"/><circle cx="100" cy="9" r="2.4"/><circle cx="112" cy="9" r="2.4"/><circle cx="124" cy="9" r="2.4"/><circle cx="136" cy="9" r="2.4"/><circle cx="148" cy="9" r="2.4"/>
    </g>
  </svg>
  <div class="lines">
    <span></span><span></span><span></span><span></span><span></span><span></span><span></span><span></span><span></span><span></span><span></span>
  </div>
  <div class="band"><span class="black"></span><span class="red"></span></div>
</article>

<article class="item slip">
  <div class="brand">
    <div class="wordmark">Brenvik</div>
    <div class="tagline">Tape and Packaging Specialists</div>
  </div>
  <div class="contact">
    <div>418 Kestrel Row</div>
    <div>Halden, ON L4K 2R9</div>
    <div class="gap"></div>
    <div class="row"><span class="dot"></span>905 555 0147</div>
    <div class="row"><span class="dot"></span>mara.quell@brenvik.com</div>
    <div class="row"><span class="dot"></span>www.brenvik.com</div>
  </div>
  <div class="band"><span class="black"></span><span class="red"></span></div>
</article>

<article class="item envelope">
  <svg class="flap" viewBox="0 0 299 37" aria-hidden="true">
    <polygon points="0,0 299,0 284,37 11,37" fill="#0d0d0d"/>
  </svg>
  <div class="brand">
    <div class="wordmark on-dark">Brenvik</div>
    <div class="tagline on-dark">Tape and Packaging Specialists</div>
  </div>
</article>

</body>
</html>
```